Harbor Oncology Partners Patient Referral Card

We need a 3.75" wide by 8.25" long patient referral card that a physician will fill out to refer their patient to Harbor Oncology Partners. The front of the card will have our logo on top, followed by contact information, a map that shows the office location and then there will be descriptive text at the bottom. On the back side, there will be a headshot photo with a brief bio of Dr. Marcus Whitfield. The address for the office is: 4175 N. Larchmont, Puyallup, WA 98461. The office phone number is 253.400.7218 and the website address is: harboroncologyhub.com

Target Market(s)

Physicians and medical staff

Font styles to use
Serif

Colors
34a7d8
33b8a4
9bcb3c

Requirements
Must have
• A map of the office location and two text boxes for descriptive language about services, and a photo and bio of Dr. Marcus Whitfield
Nice to have
• Clean and distinct design that is eye catching
Should not have
• Flowery or bold colors that distract from the content and purpose of the card

```html
<!DOCTYPE html>
<html lang="en">
<head>
<meta charset="utf-8">
<title>Harbor Oncology Partners – Patient Referral Card</title>
<link href="https://fonts.googleapis.com/css2?family=Libre+Baskerville:ital,wght@0,400;1,400&family=Nunito+Sans:ital,wght@0,400;0,700;1,300&display=swap" rel="stylesheet">
<style>
  :root {
    --page: #e6e6e6;
    --card: #ffffff;
    --teal: #22b3c3;
    --blue: #34a7d8;
    --green: #6abf4b;
    --ink: #4d4d4d;
    --ink-soft: #5c5c5c;
    --rule: #c8c8c8;
    --map-light: #f3f3f3;
    --map-dark: #e4e4e4;
    --photo-light: #9a9c9f;
    --photo-dark: #2f3033;
  }
  * { margin: 0; padding: 0; box-sizing: border-box; }
  html, body { width: 1135px; height: 1200px; overflow: hidden; background: var(--page); }
  .canvas { position: relative; width: 1135px; height: 1200px; }
  .card {
    position: absolute; top: 38px; width: 512px; height: 1124px;
    background: var(--card); overflow: hidden;
    font-family: "Nunito Sans", Arial, sans-serif;
  }
  .card--front { left: 38px; }
  .card--back { left: 586px; }

  /* Front */
  .brand__dot {
    position: absolute; left: 54px; top: 94px;
    width: 100px; height: 100px; border-radius: 50%; background: var(--teal);
  }
  .brand__name {
    position: absolute; left: 180px; top: 51px;
    font-family: "Libre Baskerville", Georgia, serif; font-weight: 400;
    font-size: 50px; line-height: 62px; letter-spacing: 1px; color: var(--teal);
    white-space: nowrap;
  }
  .tagline {
    position: absolute; left: 54px; top: 248px;
    font-size: 17px; line-height: 22px; letter-spacing: 12.5px; color: var(--ink); white-space: nowrap;
  }
  .referral-line { position: absolute; left: 54px; width: 406px; height: 2px; background: var(--rule); }
  .map {
    position: absolute; left: 27px; top: 537px; width: 458px; height: 310px;
    background: linear-gradient(135deg, var(--map-light), var(--map-dark));
  }
  .front-copy { position: absolute; left: 54px; top: 868px; width: 430px; }
  .front-copy p { font-size: 21px; line-height: 28px; color: var(--ink-soft); margin-bottom: 9px; }

  .web-band {
    position: absolute; left: 0; bottom: 0; width: 100%; height: 53px;
    background: linear-gradient(90deg, var(--green), var(--blue));
    color: #fff; font-size: 20px; letter-spacing: 2px;
    display: flex; align-items: center; justify-content: center;
  }

  /* Back */
  .headshot {
    position: absolute; left: 55px; top: 53px; width: 404px; height: 515px;
    border-radius: 22px; overflow: hidden;
    background: linear-gradient(180deg, var(--photo-light) 0%, #6c6e72 45%, var(--photo-dark) 100%);
  }
  .headshot::after {
    content: ""; position: absolute; left: 0; bottom: 0; width: 100%; height: 5px;
    background: linear-gradient(90deg, var(--green), var(--blue));
  }
  .doctor { position: absolute; left: 0; top: 585px; width: 100%; text-align: center; }
  .doctor__name { font-family: "Libre Baskerville", Georgia, serif; font-weight: 400; font-size: 29px; color: var(--teal); line-height: 40px; }
  .doctor__specialty { font-family: "Libre Baskerville", Georgia, serif; font-style: italic; font-size: 24px; color: var(--ink); line-height: 34px; }
  .bio {
    position: absolute; left: 56px; top: 677px; width: 440px;
    font-style: italic; font-weight: 300; font-size: 23px; line-height: 34px; color: var(--ink-soft);
    white-space: nowrap;
  }
  .divider { position: absolute; left: 28px; top: 904px; width: 458px; height: 2px; background: var(--teal); }
  .contact-icon { position: absolute; fill: var(--teal); }
  .contact-icon--pin { left: 83px; top: 945px; }
  .contact-icon--phone { left: 82px; top: 1015px; }
  .contact-text {
    position: absolute; left: 126px; color: var(--teal);
    font-weight: 700; font-size: 20px; letter-spacing: 1.8px; line-height: 27px; white-space: nowrap;
  }
  .contact-text--address { top: 932px; }
  .contact-text--phone { top: 1013px; }
</style>
</head>
<body>
<div class="canvas">

  <section class="card card--front">
    <div class="brand__dot"></div>
    <div class="brand__name">Harbor<br>Oncology<br>Partners</div>
    <div class="tagline">RADIATION ONCOLOGY</div>

    <div class="referral-line" style="top:376px"></div>
    <div class="referral-line" style="top:429px"></div>
    <div class="referral-line" style="top:483px"></div>

    <div class="map" role="img" aria-label="Street map showing the office at 4175 N. Larchmont, Puyallup"></div>

    <div class="front-copy">
      <p>Lorem ipsum dolor sit amet, consectetur adipiscing elit. Aenean vel nibh vitae est aliquet faucibus iaculis sed.</p>
      <p>Lorem ipsum dolor sit amet, consectetur adipiscing elit. Aenean vel nibh vitae est aliquet faucibus iaculis sed.</p>
    </div>

    <div class="web-band">www.harboroncologyhub.com</div>
  </section>

  <section class="card card--back">
    <div class="headshot" role="img" aria-label="Headshot of Dr. Marcus Whitfield"></div>

    <div class="doctor">
      <h1 class="doctor__name">Marcus Whitfield, MD PhD</h1>
      <p class="doctor__specialty">Radiation Oncology</p>
    </div>

    <p class="bio">Lorem ipsum dolor sit amet, consecte-<br>tur adipiscing elit. Aenean vel nibh<br>vitae est aliquet faucibus iaculis sed<br>sem. Pellentesque tristique ipsum et<br>sodales hendrerit. Proin nec justo<br>molestie, sodales tellus at, scelerisque.</p>

    <div class="divider"></div>

    <svg class="contact-icon contact-icon--pin" width="22" height="31" viewBox="0 0 24 32" aria-hidden="true"><path d="M12 0C5.4 0 0 5.2 0 11.7 0 20 12 32 12 32s12-12 12-20.3C24 5.2 18.6 0 12 0zm0 17a5.5 5.5 0 1 1 0-11 5.5 5.5 0 0 1 0 11z"/></svg>
    <p class="contact-text contact-text--address">4175 N. Larchmont, Puyallup,<br>WA 98461</p>

    <svg class="contact-icon contact-icon--phone" width="27" height="27" viewBox="0 0 24 24" aria-hidden="true"><path d="M6.6 10.8a15.1 15.1 0 0 0 6.6 6.6l2.2-2.2c.3-.3.7-.4 1-.2 1.1.4 2.3.6 3.6.6.6 0 1 .4 1 1V20c0 .6-.4 1-1 1C10.6 21 3 13.4 3 4c0-.6.4-1 1-1h3.5c.6 0 1 .4 1 1 0 1.3.2 2.5.6 3.6.1.3 0 .7-.2 1z"/></svg>
    <p class="contact-text contact-text--phone">253.400.7218</p>

    <div class="web-band">www.harboroncologyhub.com</div>
  </section>

</div>
</body>
</html>
```